Direct Mail Card for Septic Pumping Company

We need a two-sided, 4x6 direct mailer card for a septic pumping company called Corbin Hale Drainage Services. The card is a coupon for $20 off a free standard septic system pumping, and should entice the card's receivers to call Corbin Hale and schedule a pumping prior to December 31.

The card should complement the company website's look and feel (chdrs.com), and the design should match the holiday-oriented nature of the copy (keep the Christmas feel subtle and elegant).

The attached "wireframes" are not meant to dictate the design, but rather provide inspiration.
Updates

Project Deadline Extended
Reason: Hello all. My client will need a couple more days for final approval, so I am extending the contest until Wednesday. Thanks!

FYI, all:

Thanks to everybody for so many great designs. Tomorrow (Monday) around noon I will be submitting most of these to my client to make a final selection, and there may be a slight modification or two requested to the final selection. I appreciate everybody's participation.

Glen

Thanks to everybody for the great submissions. Our client honestly liked each of them. I appreciate all the effort that went into the project, and hope you will all consider working with us again on future projects.

Regards,

Glen

Target Market(s)

Homeowners whose homes have standard septic systems. Homeowners who know they need their tank pumped, and who are planning to have family over for the holidays.

Industry/Entity Type

It Company

Requirements
Must have
• The copy included in the attached files. A look and feel similar to the company's website (chdrs.com).

The phone number to use on the card is 555.604.1187

Bleed area needs to be 1/8" on all sides.

```html
<!DOCTYPE html>
<html lang="en">
<head>
<meta charset="utf-8">
<title>Corbin Hale Drainage Services – Holiday Pumping Coupon</title>
<link rel="stylesheet" href="https://fonts.googleapis.com/css2?family=Bubblegum+Sans&family=Oranienbaum&family=Tinos&display=swap">
<style>
  :root {
    --sky-top: #c9dcf5;
    --sky-mid: #a8c5ee;
    --sky-low: #8fb2e6;
    --stripe: rgba(255,255,255,0.12);
    --scallop: #eef4fc;
    --cream: #f6f2b8;
    --ink-blue: #2d5bb0;
    --deep-blue: #1f4f9e;
    --fine-print: #24304a;
    --brand-dark: #1b1b1b;
    --brand-red: #e3161b;
    --gold: #d6a94a;
    --holly: #5f9e33;
    --truck: #d8dde3;
  }
  * { box-sizing: border-box; margin: 0; padding: 0; }
  html, body { width: 1200px; height: 800px; overflow: hidden; }
  body { background: var(--sky-mid); }

  .card {
    position: relative;
    width: 1200px;
    height: 800px;
    overflow: hidden;
    background:
      repeating-linear-gradient(180deg, var(--stripe) 0 3px, transparent 3px 7px),
      linear-gradient(180deg, var(--sky-top) 0%, var(--sky-mid) 45%, var(--sky-low) 100%);
  }

  .scallop-band { position: absolute; left: 0; top: 118px; width: 1200px; height: 40px; }

  .holiday-ornament {
    position: absolute; left: 487px; top: 30px; width: 233px; height: 105px;
    background: linear-gradient(180deg, rgba(255,255,255,0.35), rgba(201,37,43,0.55));
    border-radius: 0 0 40px 40px;
  }

  .coupon { position: absolute; filter: drop-shadow(6px 8px 4px rgba(40,60,100,0.45)); }
  .coupon svg { position: absolute; inset: 0; }
  .coupon-offer { left: 47px; top: 150px; width: 490px; height: 395px; transform: rotate(-1deg); }
  .coupon-message { left: 513px; top: 138px; width: 665px; height: 380px; transform: rotate(-3deg); }

  .offer-amount {
    position: absolute; left: 0; width: 400px; top: 58px; text-align: center;
    font: 84px/1 "Bubblegum Sans", cursive;
    color: var(--ink-blue);
    text-shadow: 0 -3px 0 #fff;
  }
  .offer-service {
    position: absolute; left: 0; width: 400px; top: 150px; text-align: center;
    font: 48px/1 "Bubblegum Sans", cursive; color: var(--ink-blue);
  }
  .offer-call {
    position: absolute; left: 0; width: 420px; top: 228px; text-align: center;
    font: 46px/1 "Oranienbaum", serif; color: var(--deep-blue);
  }
  .offer-tagline {
    position: absolute; left: 20px; width: 460px; top: 306px; text-align: center;
    font: 30px/1 "Oranienbaum", serif; color: var(--deep-blue);
    transform: rotate(-3deg);
  }

  .message-headline {
    position: absolute; left: 30px; top: 50px; width: 470px; text-align: center;
    font: 38px/1.15 "Bubblegum Sans", cursive; color: var(--ink-blue);
    transform: rotate(-4deg);
  }
  .message-body {
    position: absolute; left: 18px; top: 148px; width: 560px; text-align: center;
    font: 27px/1.2 "Oranienbaum", serif; color: var(--deep-blue);
    white-space: nowrap;
    transform: rotate(-4deg);
  }
  .service-truck {
    position: absolute; left: 395px; top: 250px; width: 260px; height: 120px;
    background: linear-gradient(180deg, var(--truck), #9aa6b2);
    border-radius: 12px;
    transform: rotate(3deg);
  }

  .snowflake-badge {
    position: absolute; border-radius: 50%;
    background: radial-gradient(circle, #8cc257, var(--holly));
    border: 4px solid var(--cream);
  }
  .badge-offer { left: 436px; top: 150px; width: 76px; height: 76px; }
  .badge-message { left: 1036px; top: 84px; width: 86px; height: 86px; }

  .gold-garland {
    position: absolute;
    background: linear-gradient(135deg, rgba(214,169,74,0.85), rgba(214,169,74,0.35));
    border-radius: 30px;
  }
  .garland-offer { left: 340px; top: 160px; width: 110px; height: 50px; transform: rotate(-12deg); }
  .garland-corner { left: 1118px; top: 0; width: 70px; height: 290px; border-radius: 0 0 35px 35px; }

  .terms {
    position: absolute; left: 40px; top: 582px; list-style: none;
    font: 21px/26.5px "Tinos", serif; color: var(--fine-print);
  }

  .brand {
    position: absolute; left: 690px; top: 600px; width: 400px;
    display: flex; align-items: center; gap: 16px;
  }
  .brand-mark { width: 34px; height: 34px; background: var(--brand-red); flex: none; }
  .brand-name { font: 44px/1.05 "Bubblegum Sans", cursive; color: var(--brand-dark); }
</style>
</head>
<body>
<main class="card">
  <svg class="scallop-band" viewBox="0 0 1200 40" aria-hidden="true">
    <path fill="var(--scallop)" d="M0 0 H1200 V22
      q-15 14 -30 0 q-15 14 -30 0 q-15 14 -30 0 q-15 14 -30 0 q-15 14 -30 0 q-15 14 -30 0 q-15 14 -30 0 q-15 14 -30 0 q-15 14 -30 0 q-15 14 -30 0
      q-15 14 -30 0 q-15 14 -30 0 q-15 14 -30 0 q-15 14 -30 0 q-15 14 -30 0 q-15 14 -30 0 q-15 14 -30 0 q-15 14 -30 0 q-15 14 -30 0 q-15 14 -30 0
      q-15 14 -30 0 q-15 14 -30 0 q-15 14 -30 0 q-15 14 -30 0 q-15 14 -30 0 q-15 14 -30 0 q-15 14 -30 0 q-15 14 -30 0 q-15 14 -30 0 q-15 14 -30 0
      q-15 14 -30 0 q-15 14 -30 0 q-15 14 -30 0 q-15 14 -30 0 q-15 14 -30 0 q-15 14 -30 0 q-15 14 -30 0 q-15 14 -30 0 q-15 14 -30 0 q-15 14 -30 0 Z"/>
  </svg>

  <div class="holiday-ornament" role="img" aria-label="Merry Christmas ribbon with red bow and gold stars"></div>

  <section class="coupon coupon-offer">
    <svg viewBox="0 0 490 395" aria-hidden="true">
      <rect x="12" y="12" width="466" height="371" fill="var(--cream)" stroke="var(--cream)" stroke-width="18" stroke-linecap="round" stroke-dasharray="0 19"/>
    </svg>
    <p class="offer-amount">$20 OFF</p>
    <p class="offer-service">septic pumping</p>
    <p class="offer-call">Call XXX.XXX.XXX</p>
    <p class="offer-tagline">Over 75 years of delighted customers !</p>
  </section>

  <section class="coupon coupon-message">
    <svg viewBox="0 0 665 380" aria-hidden="true">
      <rect x="12" y="12" width="641" height="356" fill="var(--cream)" stroke="var(--cream)" stroke-width="18" stroke-linecap="round" stroke-dasharray="0 19"/>
    </svg>
    <h1 class="message-headline">Don’t let your septic system<br>crash your holiday party !</h1>
    <p class="message-body">If your standard septic tank hasn’t been pumped for<br>3-5 years,it may be in danger of clugging or failure.</p>
    <div class="service-truck" role="img" aria-label="White septic pumping truck with a steel tank"></div>
  </section>

  <div class="gold-garland garland-offer" role="img" aria-label="Gold bead garland"></div>
  <div class="gold-garland garland-corner" role="img" aria-label="Gold bead garland hanging from the top corner"></div>
  <div class="snowflake-badge badge-offer" role="img" aria-label="Green snowflake ornament"></div>
  <div class="snowflake-badge badge-message" role="img" aria-label="Green snowflake ornament"></div>

  <ul class="terms">
    <li>Offer applies to standard systems only.</li>
    <li>Offer good through 12/31/2013.Trip charge may apply.</li>
    <li>Cannot be applied toward services other than pumping.</li>
    <li>Cannot be combined with other offers.</li>
    <li>One Coupon per household.</li>
    <li>Not redeemable for cash.</li>
  </ul>

  <div class="brand">
    <span class="brand-mark" aria-hidden="true"></span>
    <p class="brand-name">Corbin Hale Drainage Services</p>
  </div>
</main>
</body>
</html>
```